Broschüre
Zielgruppe
Firmen und Privatpersonen
Unsere Zielkunden sind im bereich Firmen
Firmen die etwas für die Umwelt tun wollen oder sich einen Grünen anstrich geben wollen
Privatpersonen hier ist es die Gruppe die sich für den erhalt der Natur einsetzten die Bienen oder Naturprojekte unterstützen wollen und dergleichen. In der regel Menschen die BIO Kaufen
Aufgabenstellung
Standard Falzflyer DIN-A4 4 Seiten / Logo vorhanden / Unbedingt noch ein Freifeld zum ausfüllen zum bestellen. Daten die wir zum bestellen benötigen Name/Adresse/Telefonnummer/E-Mail/Unterschrift

```html
<!DOCTYPE html>
<html lang="de">
<head>
<meta charset="utf-8">
<title>BlütenHeld Falzflyer</title>
<link rel="stylesheet" href="https://fonts.googleapis.com/css2?family=Crimson+Text:wght@400;700&display=swap">
<style>
  :root {
    --honey: #ffd663;
    --ink: #1a1a1a;
    --brand: #7a3b12;
    --brand-dot: #f2b51c;
    --paper: #ffffff;
    --rule: #222222;
    --leaf-light: #e3ec9a;
    --leaf-mid: #a9cf55;
    --leaf-deep: #5f9a2e;
  }
  * { margin: 0; padding: 0; box-sizing: border-box; }
  html, body { width: 1200px; height: 800px; overflow: hidden; background: var(--paper); }
  body { font-family: "Crimson Text", serif; color: var(--ink); }
  .flyer { position: relative; width: 1200px; height: 800px; overflow: hidden; }
  .band { position: absolute; left: 0; width: 1200px; background: var(--honey); border-top: 1.5px solid var(--rule); border-bottom: 1.5px solid var(--rule); }
  .band--top { top: 0; height: 48px; }
  .band--bottom { top: 161px; height: 15px; }
  .brand { position: absolute; top: 95px; display: flex; align-items: center; gap: 10px; }
  .brand__dot { width: 30px; height: 30px; border-radius: 50%; background: var(--brand-dot); }
  .brand__name { font-weight: 700; font-size: 30px; color: var(--brand); }
  .fold-line { position: absolute; left: 413px; top: 176px; }
  .order-form__title { position: absolute; left: 46px; top: 190px; width: 362px; font-size: 23px; line-height: 30px; font-weight: 400; }
  .order-form__title strong { font-weight: 700; }
  .field { position: absolute; left: 46px; width: 362px; }
  .field__label { font-size: 14px; line-height: 18px; }
  .field__line { margin-top: 19px; border-bottom: 1.5px dashed var(--rule); }
  .consent { position: absolute; left: 46px; top: 708px; width: 352px; font-size: 13.5px; line-height: 18px; }
  .panel-caption { position: absolute; font-size: 14.5px; }
  .contact { position: absolute; left: 416px; width: 364px; top: 343px; text-align: center; font-size: 21.5px; line-height: 29px; font-style: normal; }
  .cover-claim { position: absolute; left: 806px; top: 222px; font-size: 17px; }
  .cover-offer { position: absolute; left: 806px; top: 262px; width: 362px; font-size: 14px; line-height: 19px; }
  .cover-photo { position: absolute; left: 808px; top: 349px; width: 364px; height: 350px;
    background: linear-gradient(155deg, var(--leaf-light) 0%, var(--leaf-mid) 50%, var(--leaf-deep) 100%); }
</style>
</head>
<body>
<div class="flyer">
  <div class="band band--top"></div>
  <div class="band band--bottom"></div>

  <div class="brand" style="left:24px"><span class="brand__dot"></span><span class="brand__name">BlütenHeld</span></div>
  <div class="brand" style="left:434px"><span class="brand__dot"></span><span class="brand__name">BlütenHeld</span></div>
  <div class="brand" style="left:816px"><span class="brand__dot"></span><span class="brand__name">BlütenHeld</span></div>

  <svg class="fold-line" width="6" height="560" viewBox="0 0 6 560" aria-hidden="true">
    <line x1="3" y1="0" x2="3" y2="560" stroke="#222" stroke-width="2.5" stroke-dasharray="14 28"/>
  </svg>

  <h2 class="order-form__title">Ja, ich möchte helfen und ein<br><strong>BlütenHeld</strong> werden</h2>

  <div class="field" style="top:300px"><p class="field__label">Name:</p><div class="field__line"></div></div>
  <div class="field" style="top:354px"><p class="field__label">Vorname:</p><div class="field__line"></div></div>
  <div class="field" style="top:408px"><p class="field__label">Straße und Hausnummer:</p><div class="field__line"></div></div>
  <div class="field" style="top:462px"><p class="field__label">PLZ und Ort:</p><div class="field__line"></div></div>
  <div class="field" style="top:516px"><p class="field__label">E-Mailadresse:</p><div class="field__line"></div></div>
  <div class="field" style="top:570px"><p class="field__label">Telefonnummer:</p><div class="field__line"></div></div>
  <div class="field" style="top:638px"><p class="field__label">Datum / Unterschrift:</p><div class="field__line"></div></div>

  <p class="consent">Mit Ihrer Unterschrift klären Sie sich zur Speicherung und internen Verwendung Ihrer Daten einverstanden</p>

  <p class="panel-caption" style="left:46px;top:776px">Innenseite zum Heraustrennen für die Anmeldung</p>
  <p class="panel-caption" style="left:416px;top:776px">Rückseite</p>
  <p class="panel-caption" style="left:802px;top:770px">Vorderseite</p>

  <address class="contact">
    Wabenfeld GmbH<br>
    Lindenweg 14<br>
    7123 Blumenau am See<br>
    Tel. +4369900012345<br>
    Email: post@bluetenheld.at<br>
    www.Bluetenheld.at
  </address>

  <p class="cover-claim">Saisonarbeiter, die wirklich helfen!</p>
  <p class="cover-offer">Bienenstöcke zum Mieten - wir bestäuben Ihre Bäume, Sie erhalten den Lohn</p>
  <div class="cover-photo" role="img" aria-label="Foto: Biene auf einer rosa Blüte vor grünem Hintergrund"></div>
</div>
</body>
</html>
```